Business card Zottelgarten

Business card is for a self-employed dog trainer with own dog school. Name and logo of the dog school are available. Color specifications as well. The design should be classy and minimalist, but also modern. An already existing idea would be: Front: Only the logo Back: Contact data

Font styles to use
Serif
Sans Serif
Other font styles liked:
• Trajan Pro

Colors
f78f20

Requirements
Must have
• Name: Margit Wendler-Rasch Title: Dipl. Dog Trainer Contain my logo Follow my font and color preferences (see files)

```html
<!DOCTYPE html>
<html lang="en">
<head>
<meta charset="utf-8">
<title>Zottelgarten – Business Card</title>
<link rel="stylesheet" href="https://fonts.googleapis.com/css2?family=Cinzel:wght@400;600&family=Open+Sans:wght@400;600&display=swap">
<style>
  :root {
    --orange: #f78f20;
    --charcoal: #231f20;
    --white: #ffffff;
    --text-light: #f2f2f2;
    --divider: #8a8a8a;
    --backdrop: #2b2b2b;
  }
  * { box-sizing: border-box; margin: 0; padding: 0; }
  html, body {
    width: 1200px; height: 1200px; overflow: hidden;
    background: var(--backdrop);
  }
  .sheet {
    width: 1200px; height: 1200px;
    display: flex; flex-direction: column;
    align-items: center; justify-content: center; gap: 40px;
  }
  .card {
    width: 900px; height: 540px; position: relative;
    box-shadow: 0 10px 30px rgba(0,0,0,.45);
  }

  /* Front */
  .card--front {
    background: var(--orange);
    display: flex; align-items: center; justify-content: center;
  }
  .brand { display: flex; align-items: center; gap: 28px; }
  .brand__name {
    font-family: "Cinzel", serif; font-weight: 400;
    font-size: 64px; letter-spacing: 3px; color: var(--white);
  }
  .brand__circle {
    width: 150px; height: 150px; border-radius: 50%;
    background: var(--white);
  }

  /* Back */
  .card--back { background: var(--charcoal); }
  .person { position: absolute; left: 80px; top: 110px; }
  .person__name {
    font-family: "Cinzel", serif; font-weight: 400;
    font-size: 32px; letter-spacing: 1px; color: var(--orange);
  }
  .person__title {
    font-family: "Open Sans", sans-serif; font-size: 20px;
    color: var(--text-light); margin-top: 6px;
  }
  .divider {
    position: absolute; left: 440px; top: 230px;
    width: 1px; height: 190px;
    background: linear-gradient(to bottom, transparent, var(--divider) 20%, var(--divider) 80%, transparent);
  }
  .contacts {
    position: absolute; left: 480px; top: 250px;
    list-style: none;
    font-family: "Open Sans", sans-serif; font-size: 22px;
    color: var(--text-light); line-height: 1.5;
  }
  .contacts li { display: flex; align-items: center; gap: 12px; }
  .contacts svg { width: 18px; height: 18px; flex: none; fill: var(--orange); }
</style>
</head>
<body>
<main class="sheet">
  <section class="card card--front" aria-label="Card front">
    <div class="brand">
      <span class="brand__circle" aria-hidden="true"></span>
      <span class="brand__name">ZOTTELGARTEN</span>
    </div>
  </section>

  <section class="card card--back" aria-label="Card back">
    <div class="person">
      <h1 class="person__name">MARGIT WENDLER-RASCH</h1>
      <p class="person__title">Dipl. Dog Trainer</p>
    </div>
    <div class="divider"></div>
    <ul class="contacts">
      <li>
        <svg viewBox="0 0 24 24" aria-hidden="true"><path d="M6.6 10.8a15.1 15.1 0 0 0 6.6 6.6l2.2-2.2a1 1 0 0 1 1-.25 11.4 11.4 0 0 0 3.6.57 1 1 0 0 1 1 1V20a1 1 0 0 1-1 1A17 17 0 0 1 3 4a1 1 0 0 1 1-1h3.5a1 1 0 0 1 1 1c0 1.25.2 2.45.57 3.57a1 1 0 0 1-.25 1z"/></svg>
        123 456 7890
      </li>
      <li>
        <svg viewBox="0 0 24 24" aria-hidden="true"><path d="M7 2h10a2 2 0 0 1 2 2v16a2 2 0 0 1-2 2H7a2 2 0 0 1-2-2V4a2 2 0 0 1 2-2zm0 3v13h10V5zm5 14.2a1 1 0 1 0 0 .01z"/></svg>
        123 456 7890
      </li>
      <li>
        <svg viewBox="0 0 24 24" aria-hidden="true"><path d="M3 5h18a1 1 0 0 1 1 1v12a1 1 0 0 1-1 1H3a1 1 0 0 1-1-1V6a1 1 0 0 1 1-1zm1 2.4V17h16V7.4l-8 5.3zM5.2 7 12 11.5 18.8 7z"/></svg>
        margit@zottelgarten.ch
      </li>
      <li>
        <svg viewBox="0 0 24 24" aria-hidden="true"><path d="M12 2a10 10 0 1 0 0 20 10 10 0 0 0 0-20zm0 2c.9 0 2.2 1.8 2.8 5H9.2C9.8 5.8 11.1 4 12 4zm-3 7h6a20 20 0 0 1 0 2H9a20 20 0 0 1 0-2zm-4.9 0h2.9a22 22 0 0 0 0 2H4.1a8 8 0 0 1 0-2zm12.9 0h2.9a8 8 0 0 1 0 2H17a22 22 0 0 0 0-2zM9.2 15h5.6c-.6 3.2-1.9 5-2.8 5s-2.2-1.8-2.8-5z"/></svg>
        www.zottelgarten.ch
      </li>
    </ul>
  </section>
</main>
</body>
</html>
```